Tarrowby Builders Business Card Design

We require a business Card for a new Building Company called Tarrowby Builders. We are General Builders that specialize in Industrial, Commercial and Domestic building work. We would like to see a design that incorporates Blue ,Red and White as the colour scheme and a design that will highlight a building theme.
(Once this design is achieved will need to incorporate this for the other side of the business which is Tarrowby Joinery )

Contact Information for Business Card

TARROWBY BUILDERS
17 Wendaree Rd Brindale SA 5372
Mobile 0427390548
Telephone 08 85047316
Marcus Delroy
Director / Supervisor

```html
<!DOCTYPE html>
<html lang="en">
<head>
<meta charset="utf-8">
<title>Tarrowby Builders Business Card</title>
<link href="https://fonts.googleapis.com/css2?family=Questrial&display=swap" rel="stylesheet">
<style>
  :root {
    --bg: #e9e6e1;
    --card-dark: #1f1f20;
    --card-dark-2: #3a3a3c;
    --card-light: #f4f4f4;
    --card-light-2: #e4e4e4;
    --ink: #3b3b3b;
    --red: #e2474b;
    --blue: #3f7fd6;
    --white: #ffffff;
  }
  * { margin: 0; padding: 0; box-sizing: border-box; }
  html, body {
    width: 720px; height: 1200px; overflow: hidden;
    background: var(--bg);
    font-family: "Questrial", "Century Gothic", sans-serif;
  }
  .canvas {
    width: 720px; height: 1200px;
    display: flex; flex-direction: column; align-items: center; justify-content: center;
    gap: 120px;
  }
  .card {
    width: 600px; height: 343px; position: relative; overflow: hidden;
    box-shadow: 0 10px 28px rgba(0,0,0,.25);
  }
  .card-front { background: var(--card-dark); }
  .front-info {
    position: absolute; left: 0; top: 0; width: 100%; height: 178px;
    background: linear-gradient(180deg, var(--card-light), var(--card-light-2));
    padding: 34px 40px 0 40px;
    display: flex; justify-content: space-between;
  }
  .person-name { font-size: 30px; color: var(--ink); letter-spacing: .5px; white-space: nowrap; }
  .person-role { font-size: 16px; color: var(--red); margin-top: 6px; white-space: nowrap; }
  .contact-list { list-style: none; margin-top: 8px; }
  .contact-item {
    display: flex; align-items: center; gap: 10px;
    font-size: 14.5px; color: var(--ink); margin-bottom: 10px; white-space: nowrap;
  }
  .contact-item svg { width: 14px; height: 14px; flex: none; }
  .accent-bar {
    position: absolute; left: 0; top: 168px; width: 72px; height: 10px;
    background: var(--red);
  }
  .front-brand, .back-brand {
    position: absolute; left: 0; right: 0;
    display: flex; align-items: center; justify-content: center; gap: 14px;
  }
  .front-brand { top: 178px; bottom: 0;
    background: linear-gradient(115deg, var(--card-dark) 30%, var(--card-dark-2) 55%, var(--card-dark) 80%); }
  .brand-mark { width: 16px; height: 16px; background: var(--blue); flex: none; }
  .brand-name { color: var(--blue); letter-spacing: 5px; font-size: 28px; white-space: nowrap; }
  .card-back {
    background: linear-gradient(115deg, var(--card-dark) 25%, var(--card-dark-2) 50%, var(--card-dark) 78%);
  }
  .back-brand { top: 0; bottom: 0; }
  .back-brand .brand-name { font-size: 36px; letter-spacing: 6px; }
  .back-brand .brand-mark { width: 20px; height: 20px; }
</style>
</head>
<body>
<main class="canvas">
  <section class="card card-front">
    <div class="front-info">
      <div class="person">
        <div class="person-name">Marcus Delroy</div>
        <div class="person-role">Director / Supervisor</div>
      </div>
      <ul class="contact-list">
        <li class="contact-item">
          <svg viewBox="0 0 14 14"><path d="M7 1a4 4 0 0 1 4 4c0 3-4 8-4 8S3 8 3 5a4 4 0 0 1 4-4z" fill="var(--blue)"/><circle cx="7" cy="5" r="1.5" fill="#fff"/></svg>
          17 Wendaree Rd Brindale SA 5372
        </li>
        <li class="contact-item">
          <svg viewBox="0 0 14 14"><rect x="3.5" y="1" width="7" height="12" rx="1.2" fill="none" stroke="var(--blue)" stroke-width="1.4"/><circle cx="7" cy="11" r=".8" fill="var(--blue)"/></svg>
          0427390548
        </li>
        <li class="contact-item">
          <svg viewBox="0 0 14 14"><rect x="1" y="4" width="12" height="9" rx="1.5" fill="var(--blue)"/><path d="M2 5c0-3 10-3 10 0" fill="none" stroke="var(--blue)" stroke-width="1.6"/><circle cx="7" cy="8.5" r="2" fill="#fff"/></svg>
          08 85047316
        </li>
        <li class="contact-item">
          <svg viewBox="0 0 14 14"><rect x="1" y="3" width="12" height="8" fill="var(--blue)"/><path d="M1 3l6 5 6-5" fill="none" stroke="#fff" stroke-width="1"/></svg>
          office@tarrowby.example
        </li>
      </ul>
    </div>
    <div class="accent-bar"></div>
    <div class="front-brand">
      <span class="brand-mark"></span>
      <span class="brand-name">TARROWBY BUILDERS</span>
    </div>
  </section>

  <section class="card card-back">
    <div class="back-brand">
      <span class="brand-mark"></span>
      <span class="brand-name">TARROWBY BUILDERS</span>
    </div>
  </section>
</main>
</body>
</html>
```